Business Card Design - Brightfold Dwellings

Hi there,

We would like a business card for our new venture, Brightfold Dwellings.

We are based in Western Australia and specialise in taking tired, old properties and making them look new again. We aim to create enjoyably liveable homes for young families in particular.

Product pricing is mid range i.e. appliances, furnishings, fixtures (not top end but not cheap either)

Our work is primarily cosmetic renovation (approx. 80%) and the rest construction (approx 20%).

We would like a business card that conveys the following:
- clean, simplistic/minimalistic design
- modern, contemporary style
- a touch of funk/uniqueness
- appealing to both females and males
- professionalism

I have uploaded our logo in grey or green, I do not mind which one you choose to use (please use either coloured logo on the pure white background not the white on colour version).

Details to include on the business card are:
Names: Corina Maddox and Pete Okonbrie
Mobile: 0417 362 908
Email: info@brightfolddwellings.com.au
Website: www.brightfolddwellings.com.au (note: this website is currently being developed)
Note: We will provide final details such as mobile number and names on on selection of successful design)

On the other side of the card please include a line similar to "We buy tired, un-renovated properties and sell them looking new again!"

The business card will also need to include the following "ABN 47 219 635 104" which is our Australian Business Number (again the actual number will be provided on selection of successful design). We would like this number somewhere near our name Brightfold Dwellings but in much smaller text.

The purpose of the business cards will be to give to suppliers, real estate agents, people wanting assistance in locating a property in need of renovation and potential buyers.

Thank you and please let me know if you have any further questions.

```html
<!DOCTYPE html>
<html lang="en">
<head>
<meta charset="utf-8">
<title>Brightfold Dwellings – Business Card</title>
<link rel="stylesheet" href="https://fonts.googleapis.com/css2?family=Oswald:wght@500&display=swap">
<style>
  :root {
    --slate: #22323a;
    --lime: #b2f04a;
    --paper: #e6e8e8;
    --white: #ffffff;
    --rule-grey: #e1e3e4;
    --ink: #2a2a2a;
    --photo-top: #c9d3dc;
    --photo-bottom: #8fa2b4;
  }
  html, body {
    margin: 0;
    padding: 0;
    width: 1200px;
    height: 720px;
    overflow: hidden;
    background: var(--paper);
  }
  .card {
    position: relative;
    width: 1200px;
    height: 720px;
    background: var(--paper);
    font-family: "Oswald", "Arial Narrow", sans-serif;
    overflow: hidden;
  }
  .card__panel {
    position: absolute;
    inset: 0;
  }
  .brand-rule {
    position: absolute;
    left: 98px;
    top: 116px;
    width: 327px;
    height: 7px;
    background: linear-gradient(to right, var(--lime) 0 58%, var(--rule-grey) 58% 100%);
  }
  .brand-name {
    position: absolute;
    left: 94px;
    top: 140px;
    margin: 0;
    color: var(--white);
    font-weight: 500;
    font-size: 41px;
    line-height: 1;
    letter-spacing: 0.3px;
    text-transform: uppercase;
    white-space: nowrap;
  }
  .brand-abn {
    position: absolute;
    left: 97px;
    top: 200px;
    margin: 0;
    color: var(--white);
    font-weight: 500;
    font-size: 17px;
    line-height: 1;
    text-transform: uppercase;
    white-space: nowrap;
  }
  .contact-strip {
    position: absolute;
    left: 84px;
    top: 390px;
    width: 59px;
    height: 239px;
    background: var(--lime);
  }
  .contact-list {
    position: absolute;
    left: 0;
    top: 0;
    margin: 0;
    padding: 0;
    list-style: none;
  }
  .contact-list li {
    position: absolute;
    left: 0;
    width: 600px;
    height: 40px;
  }
  .contact-list .icon {
    position: absolute;
    left: 94px;
    top: 0;
    width: 40px;
    height: 40px;
  }
  .contact-list .label {
    position: absolute;
    left: 166px;
    top: 3px;
    color: var(--white);
    font-weight: 500;
    font-size: 22px;
    line-height: 34px;
    text-transform: uppercase;
    white-space: nowrap;
  }
  .contact-list .names { top: 410px; }
  .contact-list .phone { top: 462px; }
  .contact-list .email { top: 518px; }
  .contact-list .web   { top: 574px; }
  .logo-lockup {
    position: absolute;
    left: 640px;
    top: 196px;
    width: 500px;
    display: flex;
    align-items: center;
    justify-content: center;
    gap: 16px;
  }
  .logo-lockup__square {
    width: 30px;
    height: 30px;
    background: var(--lime);
  }
  .logo-lockup__name {
    color: var(--ink);
    font-weight: 500;
    font-size: 46px;
    line-height: 1;
    white-space: nowrap;
  }
  .project-photo {
    position: absolute;
    left: 662px;
    top: 355px;
    width: 453px;
    height: 262px;
    background: linear-gradient(to bottom, var(--photo-top), var(--photo-bottom));
  }
</style>
</head>
<body>
<main class="card">
  <svg class="card__panel" width="1200" height="720" viewBox="0 0 1200 720" aria-hidden="true">
    <path d="M0 0 H480 C540 40 545 150 505 225 C465 300 450 360 520 430 C590 500 650 600 695 720 H0 Z" fill="#22323a"/>
    <path d="M480 0 C540 40 545 150 505 225 C465 300 450 360 520 430 C590 500 650 600 695 720" fill="none" stroke="#b2f04a" stroke-width="4"/>
  </svg>

  <div class="brand-rule"></div>
  <h1 class="brand-name">Brightfold Dwellings</h1>
  <p class="brand-abn">Australian Business Number:ABN 47 219 635 104</p>

  <div class="contact-strip"></div>
  <ul class="contact-list">
    <li class="names">
      <svg class="icon" viewBox="0 0 40 40" aria-hidden="true">
        <circle cx="20" cy="13" r="8" fill="#22323a"/>
        <path d="M6 36 C6 26 12 22 20 22 C28 22 34 26 34 36 Z" fill="#22323a"/>
      </svg>
      <span class="label">Corina Maddox and Pete Okonbrie</span>
    </li>
    <li class="phone">
      <svg class="icon" viewBox="0 0 40 40" aria-hidden="true">
        <path d="M10 5 L16 5 L18 13 L14 16 C16 22 19 26 25 28 L28 24 L35 27 L35 33 C35 35 33 36 31 36 C18 34 7 23 5 10 C5 7 7 5 10 5 Z" fill="#22323a"/>
      </svg>
      <span class="label">0417 362 908</span>
    </li>
    <li class="email">
      <svg class="icon" viewBox="0 0 40 40" aria-hidden="true">
        <rect x="4" y="9" width="32" height="22" fill="#22323a"/>
        <path d="M4 9 L20 22 L36 9" fill="none" stroke="#b2f04a" stroke-width="2.5"/>
      </svg>
      <span class="label">info@brightfolddwellings.com.au</span>
    </li>
    <li class="web">
      <svg class="icon" viewBox="0 0 40 40" aria-hidden="true">
        <g fill="none" stroke="#22323a" stroke-width="5" stroke-linecap="round">
          <path d="M17 23 L11 29 C8 32 5 29 8 26 L14 20"/>
          <path d="M23 17 L29 11 C32 8 35 11 32 14 L26 20"/>
          <path d="M15 25 L25 15"/>
        </g>
      </svg>
      <span class="label">www.brightfolddwellings.com.au</span>
    </li>
  </ul>

  <div class="logo-lockup">
    <span class="logo-lockup__square"></span>
    <span class="logo-lockup__name">Brightfold Dwellings</span>
  </div>

  <div class="project-photo" role="img" aria-label="Photo of hands holding a picture of a two-storey house, half pencil sketch and half finished renovation"></div>
</main>
</body>
</html>
```